Corvane Supplies Business Card

Professional business card that stand out to our potential customers. Front and back with clean modern design

Industry/Entity Type

Oil and gas

Contact Information for Business Card

Name, address, website , office phone and cell number

Requirements
Must have
• Editable files for each employee

```html
<!DOCTYPE html>
<html lang="en">
<head>
<meta charset="utf-8">
<title>Corvane Supplies Business Card</title>
<link href="https://fonts.googleapis.com/css2?family=Roboto:wght@400;700&display=swap" rel="stylesheet">
<style>
  :root {
    --page-bg: #2b2b2d;
    --card-bg: #1e1f21;
    --card-edge: #2a2b2e;
    --front-ink: #4a4b4f;
    --brand-red: #e3262f;
    --brand-blue: #2bb3d9;
    --text-light: #f2f2f2;
    --text-muted: #cfd1d4;
  }
  * { margin: 0; padding: 0; box-sizing: border-box; }
  html, body { width: 1200px; height: 852px; overflow: hidden; }
  body {
    background: var(--page-bg);
    font-family: "Roboto", Arial, sans-serif;
    position: relative;
  }
  .card {
    position: absolute;
    top: 283px;
    width: 500px;
    height: 286px;
    border-radius: 18px;
    background: var(--card-bg);
    border: 1px solid var(--card-edge);
  }
  .card-front { left: 70px; }
  .card-back { left: 630px; }

  .front-brand {
    position: absolute;
    inset: 0;
    display: flex;
    align-items: center;
    justify-content: center;
    gap: 14px;
  }
  .front-brand .brand-square {
    width: 30px; height: 30px;
    background: var(--front-ink);
  }
  .front-brand .brand-name {
    font-weight: 700;
    font-size: 30px;
    letter-spacing: 1px;
    text-transform: uppercase;
    color: var(--front-ink);
  }

  .back-brand {
    position: absolute;
    left: 30px; top: 30px;
    display: flex;
    align-items: center;
    gap: 12px;
  }
  .back-brand .brand-square {
    width: 24px; height: 24px;
    background: var(--brand-red);
  }
  .back-brand .brand-name {
    font-weight: 700;
    font-size: 24px;
    letter-spacing: 1px;
    text-transform: uppercase;
    color: var(--text-light);
  }

  .contact {
    position: absolute;
    right: 30px; bottom: 28px;
    text-align: right;
    color: var(--text-light);
    font-size: 13px;
    line-height: 1.45;
  }
  .contact .person-name {
    color: var(--brand-blue);
    font-weight: 700;
    font-size: 19px;
    line-height: 1.2;
  }
  .contact .person-title {
    color: var(--text-muted);
    font-size: 12px;
    margin-bottom: 12px;
  }
  .contact .address { margin-bottom: 10px; }
  .contact .line {
    display: flex;
    justify-content: flex-end;
    align-items: center;
    gap: 8px;
  }
  .contact .icon {
    width: 12px; height: 12px;
    fill: var(--brand-red);
    flex: none;
  }
  .contact .icon-spacer { width: 12px; flex: none; }
</style>
</head>
<body>
  <section class="card card-front" aria-label="Card front">
    <div class="front-brand">
      <span class="brand-square"></span>
      <span class="brand-name">Corvane Supplies</span>
    </div>
  </section>

  <section class="card card-back" aria-label="Card back">
    <div class="back-brand">
      <span class="brand-square"></span>
      <span class="brand-name">Corvane Supplies</span>
    </div>

    <div class="contact">
      <p class="person-name">Dana Reeve Holt</p>
      <p class="person-title">Managing Director</p>
      <p class="address">417 Larkspur Ave Suite 2<br>Brisco, Tx 79902</p>
      <p class="line">(555)014-2287
        <svg class="icon" viewBox="0 0 24 24" aria-hidden="true"><path d="M6.6 10.8a15.1 15.1 0 0 0 6.6 6.6l2.2-2.2c.3-.3.7-.4 1-.2 1.1.4 2.3.6 3.6.6.6 0 1 .4 1 1V20c0 .6-.4 1-1 1A17 17 0 0 1 3 4c0-.6.4-1 1-1h3.5c.6 0 1 .4 1 1 0 1.3.2 2.5.6 3.6.1.3 0 .7-.2 1z"/></svg>
      </p>
      <p class="line">sales@corvanesupplies.com
        <svg class="icon" viewBox="0 0 24 24" aria-hidden="true"><path d="M2 5h20v14H2zm2 2v.5l8 5 8-5V7l-8 5z"/></svg>
      </p>
      <p class="line">www.corvanesupplies.com
        <svg class="icon" viewBox="0 0 24 24" aria-hidden="true"><path d="M12 2a10 10 0 1 0 0 20 10 10 0 0 0 0-20zm6.9 6h-3a15 15 0 0 0-1.3-3.9A8 8 0 0 1 18.9 8zM12 4c.8 1.2 1.5 2.5 1.9 4h-3.8c.4-1.5 1.1-2.8 1.9-4zM4.3 14a8 8 0 0 1 0-4h3.4a16 16 0 0 0 0 4zm.8 2h3a15 15 0 0 0 1.3 3.9A8 8 0 0 1 5.1 16zm3-8h-3a8 8 0 0 1 4.3-3.9C8.8 5.3 8.4 6.6 8.1 8zM12 20c-.8-1.2-1.5-2.5-1.9-4h3.8c-.4 1.5-1.1 2.8-1.9 4zm2.3-6H9.7a14 14 0 0 1 0-4h4.6a14 14 0 0 1 0 4zm.3 5.9c.6-1.2 1-2.5 1.3-3.9h3a8 8 0 0 1-4.3 3.9zm1.7-5.9a16 16 0 0 0 0-4h3.4a8 8 0 0 1 0 4z"/></svg>
      </p>
    </div>
  </section>
</body>
</html>
```